Crestline Sealing - Logo and Advert

Help to provide logo and advert.
Advert is to be short and concise to fit in a printed directory posted around homes.
Ideally the same advert to be able to be blown up as a leaflet.
Use of eco friendly type colours, soft greens and blues.
Logo to be subtle but indicative to roofing and facades.
Breakdown of advert as follows;
Company name:
Crestline Sealing
Sub title:
Roofing & Façades
Services breakdown:
Pitched (Slating & Tiling)
Flat (Single Ply, Liquid & Mineral Felt)
Hard Metal (Zinc Standing Seam)
Leadwork
Roof lights and lanterns
Generic notes:
100% flame free applications available, eliminating all fire risks to your property. (No gas torch’s etc.).
Expert consultation and advice.
Product warranty and/or insurance backed warranty available.
Fully insured contractor.
Contact information:
Phone number to be confirmed
Email and/or website to be confirmed.
Please feel free to try out different colours and fonts other than outlined. I am not limited to those and open to suggestions.
Target Market(s)
Domestic/Private Home Owners/Small Buidlers
Industry/Entity Type
Roofing
Font styles to use
Look and feel
Each slider illustrates characteristics of the customer's brand and the style your logo design should communicate.

```html
<!DOCTYPE html>
<html lang="en">
<head>
<meta charset="utf-8">
<title>Crestline Sealing – Roofing &amp; Façades Advert</title>
<link rel="stylesheet" href="https://fonts.googleapis.com/css2?family=Barlow+Condensed:ital,wght@0,600;0,700;1,700;1,800&family=Barlow:wght@500;600;700&family=Montserrat:wght@500;800&display=swap">
<style>
  :root {
    --navy: #1b3577;
    --navy-deep: #142a5e;
    --royal: #2a4fb0;
    --ink: #2b2b2b;
    --text: #333a40;
    --green: #7dbf3f;
    --green-deep: #4f9a2a;
    --sky-light: #e8fbfd;
    --sky: #6fe3ea;
    --mist: #eeeff1;
    --white: #ffffff;
  }
  * { margin: 0; padding: 0; box-sizing: border-box; }
  html, body { width: 960px; height: 1200px; overflow: hidden; background: var(--white); }
  .advert {
    position: relative; width: 960px; height: 1200px; overflow: hidden;
    background: linear-gradient(160deg, var(--sky-light) 0%, #c9f3f7 35%, var(--sky) 70%, #8fe6ec 100%);
    font-family: "Barlow", sans-serif;
  }
  .advert::after {
    content: ""; position: absolute; left: 0; right: 0; top: 380px; height: 600px;
    background: linear-gradient(180deg, rgba(255,255,255,0) 0%, var(--white) 22%);
    z-index: 0;
  }
  .hero-photo {
    position: absolute; left: 400px; top: 420px; width: 560px; height: 556px; z-index: 1;
    background:
      linear-gradient(90deg, var(--white) 0%, rgba(255,255,255,0) 40%),
      linear-gradient(180deg, rgba(255,255,255,0.6) 0%, rgba(255,255,255,0) 18%),
      linear-gradient(170deg, #b9cfd8 0%, #7d96a2 35%, #3f5660 65%, #2a3439 100%);
  }
  .brand {
    position: absolute; top: 118px; left: 0; width: 960px; z-index: 2;
    display: flex; justify-content: center; align-items: center; gap: 16px;
  }
  .brand-dot { width: 40px; height: 40px; border-radius: 50%; background: var(--navy); }
  .brand-name {
    font-family: "Barlow", sans-serif; font-weight: 700; font-size: 56px;
    color: var(--navy); letter-spacing: 1px; text-transform: uppercase;
  }
  .kicker {
    position: absolute; top: 250px; left: 0; width: 960px; text-align: center; z-index: 2;
    font-family: "Barlow Condensed", sans-serif; font-style: italic; font-weight: 700;
    font-size: 48px; color: var(--ink); letter-spacing: -0.5px;
  }
  .headline {
    position: absolute; top: 300px; left: 0; width: 960px; text-align: center; z-index: 2;
    font-family: "Barlow Condensed", sans-serif; font-style: italic; font-weight: 800;
    font-size: 122px; line-height: 1; letter-spacing: -2px; color: var(--royal);
    -webkit-text-stroke: 0; text-shadow: 0 0 0 var(--white),
      2px 2px 0 #dfe7ff, -2px -2px 0 #dfe7ff, 2px -2px 0 #dfe7ff, -2px 2px 0 #dfe7ff;
  }
  .services-band {
    position: absolute; top: 442px; left: 0; width: 444px; height: 52px; z-index: 2;
    background: var(--navy); clip-path: polygon(0 0, 100% 0, 97% 100%, 0 100%);
    font-family: "Barlow Condensed", sans-serif; font-style: italic; font-weight: 700;
    font-size: 34px; color: var(--white); padding-left: 48px; line-height: 52px;
  }
  .services {
    position: absolute; top: 508px; left: 42px; width: 370px; list-style: none; z-index: 2;
  }
  .services li {
    position: relative; padding-left 0; margin-left: 0;
    font-family: "Barlow", sans-serif; font-weight: 600; font-size: 26px; line-height: 32px;
    color: var(--text); padding: 5px 0 5px 50px;
  }
  .services li + li::before {
    content: ""; position: absolute; top: 0; left: 50px; right: 0; height: 1px;
    background: linear-gradient(90deg, #c9ccd0, rgba(201,204,208,0));
  }
  .services .tick { position: absolute; left: 2px; top: 9px; width: 26px; height: 26px; }
  .badges { position: absolute; top: 834px; left: 46px; display: flex; gap: 14px; z-index: 2; }
  .badge { width: 122px; height: 122px; border-radius: 50%; }
  .badge-insured { background: var(--white); border: 8px solid var(--green-deep); box-shadow: inset 0 0 0 6px var(--navy); }
  .badge-guarantee { background: radial-gradient(circle, #f7c842 0 42%, #3b3b3b 43% 66%, #e1a823 67%); }
  .notes {
    position: absolute; top: 976px; left: 0; width: 960px; height: 122px; z-index: 2;
    background: var(--mist);
  }
  .flame-free { position: absolute; left: 44px; top: 20px; }
  .flame-free h2 {
    font-family: "Barlow Condensed", sans-serif; font-weight: 700; font-size: 35px;
    line-height: 30px; color: var(--navy-deep); text-transform: uppercase;
  }
  .flame-free p { font-size: 13px; font-weight: 500; color: var(--ink); margin-top: 6px; }
  .warranty-bar {
    position: absolute; left: 540px; top: 24px; width: 420px; height: 68px;
    background: var(--green); color: var(--white);
    font-family: "Barlow Condensed", sans-serif; font-weight: 600; font-size: 24px; line-height: 25px;
    padding: 8px 0 0 38px;
  }
  .thumb-disc {
    position: absolute; left: 463px; top: 12px; width: 92px; height: 92px; border-radius: 50%;
    background: var(--green); border: 5px solid var(--white); box-shadow: 0 0 0 2px #d9dcde;
    display: flex; align-items: center; justify-content: center;
  }
  .contact-strip {
    position: absolute; top: 1098px; left: 0; width: 960px; height: 102px; z-index: 2;
    background: linear-gradient(180deg, var(--navy) 0%, var(--navy-deep) 100%);
  }
  .contact-strip .scallop { position: absolute; top: -6px; left: 0; }
  .cta-tab {
    position: absolute; left: 34px; top: -12px; width: 138px; height: 90px; z-index: 3;
    background: linear-gradient(180deg, #8ccb4a, var(--green-deep)); border-radius: 14px;
    text-align: center; color: var(--white);
  }
  .cta-tab small { display: block; font-family: "Barlow Condensed", sans-serif; font-weight: 600; font-size: 13px; margin-top: 12px; }
  .cta-tab strong { display: block; font-family: "Barlow Condensed", sans-serif; font-weight: 700; font-size: 22px; line-height: 21px; }
  .phone-icon { position: absolute; left: 180px; top: 18px; }
  .phone-block { position: absolute; left: 262px; top: 14px; color: var(--white); text-align: center; }
  .phone-number { font-family: "Montserrat", sans-serif; font-weight: 800; font-size: 40px; line-height: 44px; letter-spacing: -0.5px; }
  .phone-address { font-family: "Montserrat", sans-serif; font-weight: 500; font-size: 15px; margin-top: 2px; }
  .divider { position: absolute; left: 596px; top: 24px; width: 2px; height: 58px; background: #e2c15a; }
  .web-lines { position: absolute; left: 632px; top: 18px; list-style: none; color: var(--white); }
  .web-lines li { display: flex; align-items: center; gap: 14px; font-family: "Barlow", sans-serif; font-weight: 500; font-size: 22px; line-height: 30px; }
</style>
</head>
<body>
<main class="advert">
  <div class="hero-photo" role="img" aria-label="Roofer in work clothes laying a waterproof membrane roll on a flat roof"></div>

  <header class="brand">
    <span class="brand-dot"></span>
    <span class="brand-name">Crestline Sealing</span>
  </header>

  <p class="kicker">NEED TO PROTECT ON YOUR</p>
  <h1 class="headline">ROOFING &amp; FAÇADES</h1>

  <div class="services-band">SERVICES BREAKDOWN:</div>
  <ul class="services">
    <li><svg class="tick" viewBox="0 0 26 26"><circle cx="12" cy="14" r="10" fill="none" stroke="#7dbf3f" stroke-width="2.2"/><path d="M7 14l5 5L24 4" fill="none" stroke="#7dbf3f" stroke-width="3" stroke-linecap="round"/></svg>Pitched (Slating and Tiling)</li>
    <li><svg class="tick" viewBox="0 0 26 26"><circle cx="12" cy="14" r="10" fill="none" stroke="#7dbf3f" stroke-width="2.2"/><path d="M7 14l5 5L24 4" fill="none" stroke="#7dbf3f" stroke-width="3" stroke-linecap="round"/></svg>Flat (Single Ply, Liquid &amp; Mineral Felt)</li>
    <li><svg class="tick" viewBox="0 0 26 26"><circle cx="12" cy="14" r="10" fill="none" stroke="#7dbf3f" stroke-width="2.2"/><path d="M7 14l5 5L24 4" fill="none" stroke="#7dbf3f" stroke-width="3" stroke-linecap="round"/></svg>Hard Metal (Zinc Standing Seam)</li>
    <li><svg class="tick" viewBox="0 0 26 26"><circle cx="12" cy="14" r="10" fill="none" stroke="#7dbf3f" stroke-width="2.2"/><path d="M7 14l5 5L24 4" fill="none" stroke="#7dbf3f" stroke-width="3" stroke-linecap="round"/></svg>Leadwork</li>
    <li><svg class="tick" viewBox="0 0 26 26"><circle cx="12" cy="14" r="10" fill="none" stroke="#7dbf3f" stroke-width="2.2"/><path d="M7 14l5 5L24 4" fill="none" stroke="#7dbf3f" stroke-width="3" stroke-linecap="round"/></svg>Roof Lights &amp; Lanterns</li>
  </ul>

  <div class="badges">
    <div class="badge badge-insured" role="img" aria-label="Insured contractor badge"></div>
    <div class="badge badge-guarantee" role="img" aria-label="Satisfaction guarantee seal"></div>
  </div>

  <section class="notes">
    <div class="flame-free">
      <h2>100% Flame Free<br>Applications Available,</h2>
      <p>eliminating all fire risks to your property. (No gas torch's etc.).</p>
    </div>
    <div class="warranty-bar">Product warranty and or insurance<br>backed warranty available.</div>
    <div class="thumb-disc">
      <svg width="48" height="48" viewBox="0 0 48 48" fill="none" stroke="#fff" stroke-width="3" stroke-linejoin="round">
        <rect x="4" y="20" width="9" height="22" rx="2"/>
        <path d="M13 22l9-14c3 0 5 2 4 6l-2 7h14c3 0 4 3 3 5l-4 14c-1 2-2 2-4 2H13"/>
      </svg>
    </div>
  </section>

  <footer class="contact-strip">
    <svg class="scallop" width="960" height="8" viewBox="0 0 960 8">
      <defs><pattern id="scallop" width="16" height="8" patternUnits="userSpaceOnUse"><circle cx="8" cy="8" r="8" fill="#1b3577"/></pattern></defs>
      <rect width="960" height="8" fill="url(#scallop)"/>
    </svg>
    <div class="cta-tab"><small>For More Details</small><strong>CONTACT<br>TODAY!</strong></div>
    <svg class="phone-icon" width="62" height="60" viewBox="0 0 62 60">
      <rect x="18" y="4" width="26" height="46" rx="4" fill="none" stroke="#7dbf3f" stroke-width="4"/>
      <circle cx="31" cy="44" r="2" fill="#7dbf3f"/>
      <path d="M4 40c0-8 6-12 12-12h4v22h-6C8 50 4 46 4 40z" fill="#7dbf3f"/>
      <rect x="42" y="26" width="14" height="6" rx="3" fill="#7dbf3f"/>
      <rect x="42" y="34" width="14" height="6" rx="3" fill="#7dbf3f"/>
      <rect x="42" y="42" width="12" height="6" rx="3" fill="#7dbf3f"/>
    </svg>
    <div class="phone-block">
      <div class="phone-number">0123-456-789</div>
      <div class="phone-address">Your Company Address Goes Here</div>
    </div>
    <div class="divider"></div>
    <ul class="web-lines">
      <li><svg width="16" height="16" viewBox="0 0 16 16" fill="none" stroke="#7dbf3f" stroke-width="1.5"><circle cx="8" cy="8" r="7"/><ellipse cx="8" cy="8" rx="3" ry="7"/><path d="M1 8h14M2 4.5h12M2 11.5h12"/></svg>www.yourwebsite.com</li>
      <li><svg width="16" height="16" viewBox="0 0 16 16"><circle cx="8" cy="8" r="8" fill="#7dbf3f"/><rect x="4" y="5" width="8" height="6" fill="none" stroke="#142a5e" stroke-width="1.2"/><path d="M4 5l4 3.5L12 5" fill="none" stroke="#142a5e" stroke-width="1.2"/></svg>info@yourmailid.com</li>
    </ul>
  </footer>
</main>
</body>
</html>
```